To design a brand identity that is simple and creative with 'Valtor' as the brand name, I like modern simple fonts like helvetica neue, I want to print both sides of the card, I am open to dark front and white back, but the design needs to transfer well to letter heads and email signatures, I am looking for sophisticated and elegant, but open minded about clever and off the wall, I do not do 'boring' Valtor Holdings is the mother company for a small group, specialising in Management & consulting, Software development and construction, we have a high level of integrity, we are transparent and accountable for what we do. my images are provided as a guide only, Im not expecting them to be just copied, Im looking for a creator and passionate thinker, who will put life into their work.

Target Market(s)

usually business minded people who are looking for something different in me, such as leadership, confidence and focus with thinking that is per haps a little outside the box..

Industry/Entity Type

Construction

Requirements
Must have
• clean, minmalistic
Nice to have
• custom logo
Should not have
• boring, traditional

```html
<!DOCTYPE html>
<html lang="en">
<head>
<meta charset="utf-8">
<title>Valtor – Business Card</title>
<link href="https://fonts.googleapis.com/css2?family=Questrial&display=swap" rel="stylesheet">
<style>
  :root {
    --stage: #e9e7e4;
    --card-dark: #262626;
    --card-dark-glow: #3a3a3a;
    --card-light: #ffffff;
    --ink-light: #ffffff;
    --ink-dark: #3b3b3b;
    --ink-mid: #555555;
    --accent-yellow: #f2c21a;
    --accent-lime: #d9d22a;
    --accent-orange: #f08a1c;
    --accent-red: #e8572a;
    --font-main: "Questrial", "Century Gothic", sans-serif;
  }
  * { margin: 0; padding: 0; box-sizing: border-box; }
  html, body {
    width: 1200px; height: 1000px; overflow: hidden;
    background: var(--stage);
    font-family: var(--font-main);
  }
  .stage {
    width: 1200px; height: 1000px;
    display: flex; flex-direction: column;
    align-items: center; justify-content: center; gap: 56px;
  }
  .card {
    width: 660px; height: 377px; position: relative; overflow: hidden;
    box-shadow: 0 10px 30px rgba(0,0,0,0.22);
  }

  /* Front */
  .card-front {
    background: radial-gradient(ellipse at 45% 40%, var(--card-dark-glow) 0%, var(--card-dark) 70%);
    color: var(--ink-light);
  }
  .brand-lockup {
    position: absolute; left: 92px; top: 92px;
    display: flex; align-items: center; gap: 26px;
  }
  .brand-dot {
    width: 92px; height: 92px; border-radius: 50%;
    background: var(--accent-orange);
    flex: none;
  }
  .brand-name {
    font-size: 78px; letter-spacing: 1px; line-height: 1;
    color: var(--ink-light);
  }
  .brand-tagline {
    position: absolute; left: 92px; top: 206px;
    font-size: 34px; letter-spacing: 0.5px;
  }
  .service-list {
    position: absolute; left: 0; right: 0; bottom: 40px;
    display: flex; justify-content: center; align-items: center; gap: 28px;
    list-style: none; font-size: 20px; letter-spacing: 1px;
  }
  .service-divider {
    width: 2px; height: 16px; background: var(--accent-yellow);
  }

  /* Back */
  .card-back { background: var(--card-light); color: var(--ink-dark); }
  .company-block {
    position: absolute; right: 48px; top: 48px; text-align: right;
  }
  .company-name { font-size: 32px; letter-spacing: 1px; }
  .company-address { font-size: 21px; color: var(--ink-mid); margin-top: 10px; letter-spacing: 1.5px; }
  .person-block { position: absolute; left: 48px; top: 190px; }
  .person-name { font-size: 30px; }
  .person-role { font-size: 21px; color: var(--ink-mid); margin-top: 4px; letter-spacing: 1px; }
  .contact-list {
    position: absolute; right: 48px; top: 250px;
    list-style: none; text-align: right; font-size: 22px; letter-spacing: 1px;
  }
  .contact-item { display: flex; align-items: center; justify-content: flex-end; gap: 10px; margin-bottom: 6px; }
  .contact-icon { width: 18px; height: 18px; flex: none; }
  .accent-band {
    position: absolute; left: 0; right: 0; bottom: 0; height: 26px;
    background: linear-gradient(90deg, var(--accent-lime) 0%, var(--accent-yellow) 35%, var(--accent-orange) 70%, var(--accent-red) 100%);
  }
</style>
</head>
<body>
<main class="stage">
  <section class="card card-front" aria-label="Card front">
    <div class="brand-lockup">
      <span class="brand-dot"></span>
      <span class="brand-name">VALTOR</span>
    </div>
    <p class="brand-tagline">in the creation business..</p>
    <ul class="service-list">
      <li>management</li>
      <li class="service-divider" aria-hidden="true"></li>
      <li>software</li>
      <li class="service-divider" aria-hidden="true"></li>
      <li>construction</li>
    </ul>
  </section>

  <section class="card card-back" aria-label="Card back">
    <div class="company-block">
      <p class="company-name">VALTOR</p>
      <p class="company-address">PO BOX 418 Perth 6000</p>
    </div>
    <div class="person-block">
      <p class="person-name">Damon</p>
      <p class="person-role">Client ambassador</p>
    </div>
    <ul class="contact-list">
      <li class="contact-item">+61 0400 512 947
        <svg class="contact-icon" viewBox="0 0 18 18" aria-hidden="true">
          <rect x="4.5" y="1.5" width="9" height="15" rx="1.5" fill="none" stroke="#3b3b3b" stroke-width="1.5"/>
          <line x1="7.5" y1="13.5" x2="10.5" y2="13.5" stroke="#3b3b3b" stroke-width="1.5"/>
        </svg>
      </li>
      <li class="contact-item">damon@valtor.holdings
        <svg class="contact-icon" viewBox="0 0 18 18" aria-hidden="true">
          <rect x="1.5" y="4" width="15" height="10" fill="none" stroke="#3b3b3b" stroke-width="1.5"/>
          <polyline points="1.5,4 9,10 16.5,4" fill="none" stroke="#3b3b3b" stroke-width="1.5"/>
        </svg>
      </li>
    </ul>
    <div class="accent-band"></div>
  </section>
</main>
</body>
</html>
```